We are looking to recreate our Harlow & Partners Jobsite Sign. This sign will be placed by the street at each of our jobsites. We want to keep this sign simple, but at the same time, want to add a catching appeal to the design for anyone passing by. We want to stick to a two color scheme (Harlow Blue, and White). Please only use the Company Logo that I have uploaded for this project. Please also see a mock up of what we would like to include on this sign. The Sign Dimensions will be 4' x 8'. Please keep all verbiage uniform with the verbiage on the sample design I have uploaded. LET YOUR CREATIVITY FLOW!

```html
<!DOCTYPE html>
<html lang="en">
<head>
<meta charset="utf-8">
<title>Harlow &amp; Partners – Jobsite Sign</title>
<link rel="stylesheet" href="https://fonts.googleapis.com/css2?family=Source+Serif+4:opsz,wght@8..60,500;8..60,600&display=swap">
<style>
  :root {
    --harlow-blue: #2e3480;
    --white: #ffffff;
    --backdrop: #b1b0b5;
  }
  html, body {
    margin: 0;
    padding: 0;
    width: 900px;
    height: 1200px;
    overflow: hidden;
    background: var(--backdrop);
  }
  .canvas {
    position: relative;
    width: 900px;
    height: 1200px;
  }
  .sign {
    position: absolute;
    left: 155px;
    width: 609px;
    height: 305px;
    display: block;
    font-family: "Source Serif 4", Georgia, serif;
  }
  .sign--light { top: 201px; --paper: var(--white); --ink: var(--harlow-blue); }
  .sign--dark  { top: 690px; --paper: var(--harlow-blue); --ink: var(--white); }

  .sign__ground { fill: var(--paper); }
  .sign__accent { fill: var(--ink); }
  .sign__frame { fill: none; stroke: var(--ink); stroke-width: 3; }
  .sign__frame--on-accent { stroke: var(--paper); }

  .brand-name, .brand-trade, .tagline, .location { fill: var(--ink); font-weight: 600; }
  .brand-name { font-size: 80px; letter-spacing: -1px; }
  .brand-sub { font-size: 38px; font-weight: 500; }
  .brand-divider { stroke: var(--ink); stroke-width: 4; }
  .brand-trade { font-size: 58px; }
  .tagline { font-size: 42px; }
  .location { font-size: 29px; font-variant: small-caps; letter-spacing: 1.5px; }

  .contact { fill: var(--paper); font-weight: 500; }
  .contact__line { font-size: 19px; }
  .contact__web { font-size: 34px; }
  .social-dot { fill: var(--paper); }
</style>
</head>
<body>
<div class="canvas">

  <svg width="0" height="0" style="position:absolute" aria-hidden="true">
    <defs>
      <clipPath id="accent-area">
        <polygon points="1012,0 1123,0 1123,499 602,499"/>
        <polygon points="255,499 600,499 552,562 198,562"/>
      </clipPath>
    </defs>
  </svg>

  <!-- Light version -->
  <svg class="sign sign--light" viewBox="0 0 1123 562" role="img" aria-label="Harlow &amp; Partners jobsite sign, white version">
    <rect class="sign__ground" width="1123" height="562"/>
    <polygon class="sign__accent" points="1012,0 1123,0 1123,499 602,499"/>
    <polygon class="sign__accent" points="255,499 600,499 552,562 198,562"/>
    <rect class="sign__frame" x="22" y="22" width="1079" height="518"/>
    <rect class="sign__frame sign__frame--on-accent" x="22" y="22" width="1079" height="518" clip-path="url(#accent-area)"/>

    <g class="brand">
      <text class="brand-name" x="393" y="140" text-anchor="end">Harlow</text>
      <text class="brand-name brand-sub" x="393" y="182" text-anchor="end">&amp; Partners, Inc.</text>
      <line class="brand-divider" x1="422" y1="82" x2="422" y2="195"/>
      <text class="brand-trade" x="610" y="133" text-anchor="middle">General</text>
      <text class="brand-trade" x="610" y="180" text-anchor="middle">Contractors</text>
    </g>
    <text class="tagline" x="410" y="285" text-anchor="middle">“We Build Lasting Trust”®</text>
    <text class="location" x="389" y="459" text-anchor="middle">Lakeport, Florida</text>

    <g class="contact">
      <text class="contact__line" x="1055" y="313" text-anchor="end">555-214-0473</text>
      <text class="contact__line" x="1055" y="337" text-anchor="end">CGC4827715</text>
      <circle class="social-dot" cx="953" cy="403" r="17"/>
      <circle class="social-dot" cx="995" cy="403" r="17"/>
      <circle class="social-dot" cx="1037" cy="403" r="17"/>
      <text class="contact__web" x="1050" y="475" text-anchor="end">HarlowPartners.net</text>
    </g>
  </svg>

  <!-- Dark version -->
  <svg class="sign sign--dark" viewBox="0 0 1123 562" role="img" aria-label="Harlow &amp; Partners jobsite sign, blue version">
    <rect class="sign__ground" width="1123" height="562"/>
    <polygon class="sign__accent" points="1012,0 1123,0 1123,499 602,499"/>
    <polygon class="sign__accent" points="255,499 600,499 552,562 198,562"/>
    <rect class="sign__frame" x="22" y="22" width="1079" height="518"/>
    <rect class="sign__frame sign__frame--on-accent" x="22" y="22" width="1079" height="518" clip-path="url(#accent-area)"/>

    <g class="brand" transform="translate(-24,0)">
      <text class="brand-name" x="393" y="140" text-anchor="end">Harlow</text>
      <text class="brand-name brand-sub" x="393" y="182" text-anchor="end">&amp; Partners, Inc.</text>
      <line class="brand-divider" x1="422" y1="82" x2="422" y2="195"/>
      <text class="brand-trade" x="610" y="133" text-anchor="middle">General</text>
      <text class="brand-trade" x="610" y="180" text-anchor="middle">Contractors</text>
    </g>
    <text class="tagline" x="400" y="292" text-anchor="middle">“We Build Lasting Trust”®</text>
    <text class="location" x="401" y="459" text-anchor="middle">Lakeport, Florida</text>

    <g class="contact" transform="translate(-9,0)">
      <text class="contact__line" x="1055" y="313" text-anchor="end">555-214-0473</text>
      <text class="contact__line" x="1055" y="337" text-anchor="end">CGC4827715</text>
      <circle class="social-dot" cx="953" cy="403" r="17"/>
      <circle class="social-dot" cx="995" cy="403" r="17"/>
      <circle class="social-dot" cx="1037" cy="403" r="17"/>
      <text class="contact__web" x="1050" y="475" text-anchor="end">HarlowPartners.net</text>
    </g>
  </svg>

</div>
</body>
</html>
```